Building Company Business Card Design

Need a design for a business card:
It needs to have: Name, Phone, Facebook link, Website, email
i would also like a list of works we undertake:
-New Homes
-Extensions, Renovations & Bathrooms
-Decking, Carports, Sheds (Residential and Industrial)
-Carpentry
-Fences, Patios & Pergolas

Name, Phone, Facebook link, Website, email + details of services provided listed in description

```html
<!DOCTYPE html>
<html lang="en">
<head>
<meta charset="utf-8">
<title>Ridgeline Homes – Business Card</title>
<link href="https://fonts.googleapis.com/css2?family=Jost:wght@400;500;700&display=swap" rel="stylesheet">
<style>
  :root {
    --stage: #2e2f31;
    --green: #2fa944;
    --green-mid: #22923a;
    --green-deep: #0c5a1e;
    --green-shade: #0a4717;
    --ink: #0b0c0d;
    --ink-soft: #1a1c1d;
    --text-dark: #0d1f10;
    --text-light: #e6e8e6;
    --grey: #b9bcbc;
  }
  * { box-sizing: border-box; margin: 0; padding: 0; }
  html, body { width: 1200px; height: 900px; overflow: hidden; }
  body {
    background: var(--stage);
    font-family: "Jost", Arial, sans-serif;
    position: relative;
  }
  .card {
    position: absolute;
    width: 700px;
    height: 400px;
    overflow: hidden;
  }

  /* ---------- Services side ---------- */
  .card--services {
    left: 140px; top: 40px;
    background: linear-gradient(160deg, var(--green) 0%, var(--green-mid) 55%, var(--green) 100%);
    border-radius: 34px 34px 0 34px;
  }
  .card--services .feature {
    position: absolute; right: 0; top: 0;
    width: 330px; height: 100%;
    background: linear-gradient(200deg, var(--green-mid) 0%, var(--green-deep) 60%, var(--green-shade) 100%);
  }
  .services__body {
    position: absolute; left: 44px; top: 50px; width: 340px;
    color: var(--text-dark);
  }
  .brand {
    font-weight: 500;
    text-transform: uppercase;
    line-height: 1;
  }
  .brand__main { font-size: 40px; letter-spacing: 0.5px; }
  .brand__sub { font-size: 15.5px; letter-spacing: 0.6px; margin-top: 3px; }
  .services__rule {
    height: 1px; background: var(--text-dark); opacity: .7;
    margin: 12px 0 18px; width: 330px;
  }
  .services__title {
    font-weight: 700; font-size: 18px; letter-spacing: 1px; margin-bottom: 8px;
  }
  .services__list { list-style: none; }
  .services__list li {
    font-size: 18px; line-height: 1.5; padding-left: 22px; position: relative;
  }
  .services__list li::before {
    content: ""; position: absolute; left: 4px; top: 11px;
    width: 7px; height: 7px; background: var(--text-dark); transform: rotate(45deg);
  }

  /* ---------- Contact side ---------- */
  .card--contact {
    left: 360px; top: 480px;
    background: var(--ink);
    border-radius: 0 34px 0 34px;
  }
  .card--contact .feature {
    position: absolute; right: 0; top: 0;
    width: 320px; height: 100%;
    background: linear-gradient(200deg, var(--green-shade) 0%, #0f2a15 40%, var(--ink-soft) 100%);
  }
  .contact__body {
    position: absolute; left: 44px; top: 52px; color: var(--text-light);
  }
  .person__name {
    font-weight: 700; font-size: 30px; color: var(--green);
    letter-spacing: 1px; text-transform: uppercase; line-height: 1;
  }
  .person__role { font-size: 19px; margin-top: 6px; }
  .contact__address { font-size: 19px; line-height: 1.3; margin: 22px 0 0 24px; }
  .contact__list { list-style: none; margin: 24px 0 0 50px; }
  .contact__list li {
    display: flex; align-items: center; gap: 10px;
    font-size: 19px; line-height: 1.55;
  }
  .contact__list svg { width: 18px; height: 18px; flex: none; }
  .contact__social {
    position: absolute; left: 94px; bottom: 34px;
    display: flex; align-items: center; gap: 10px;
    color: var(--text-light); font-size: 19px;
  }
  .contact__social .dot {
    width: 18px; height: 18px; border-radius: 50%; background: var(--green);
  }
  .contact__brand {
    position: absolute; right: 36px; bottom: 70px;
    color: var(--text-light); text-align: right;
  }
  .contact__brand .brand__main { font-size: 34px; }
  .contact__brand .brand__sub { font-size: 13.5px; }
</style>
</head>
<body>

  <section class="card card--services" aria-label="Services side">
    <div class="feature" role="img" aria-label="Abstract green house-roof graphic"></div>
    <div class="services__body">
      <div class="brand">
        <div class="brand__main">Ridgeline Homes</div>
        <div class="brand__sub">and Developments Pty Ltd</div>
      </div>
      <div class="services__rule"></div>
      <h2 class="services__title">OUR SERVICES</h2>
      <ul class="services__list">
        <li>New Homes, Extensions</li>
        <li>Renovations &amp; Bathrooms</li>
        <li>Decking, Carports</li>
        <li>Sheds (Residential and Industrial)</li>
        <li>Carpentry, Fences</li>
        <li>Patios &amp; Pergolas</li>
      </ul>
    </div>
  </section>

  <section class="card card--contact" aria-label="Contact side">
    <div class="feature" role="img" aria-label="Abstract dark green house-roof graphic"></div>
    <div class="contact__body">
      <div class="person__name">John Smith</div>
      <div class="person__role">Director</div>
      <address class="contact__address" style="font-style:normal">
        00 dummy city<br>dummy place 0000
      </address>
      <ul class="contact__list">
        <li>
          <svg viewBox="0 0 24 24" fill="none" stroke="#2fa944" stroke-width="2.4" stroke-linecap="round"><path d="M5 3h4l2 5-2.5 1.5a11 11 0 0 0 6 6L16 13l5 2v4a2 2 0 0 1-2 2A16 16 0 0 1 3 5a2 2 0 0 1 2-2z"/></svg>
          000-000-0000
        </li>
        <li>
          <svg viewBox="0 0 24 24" fill="none" stroke="#2fa944" stroke-width="2.4" stroke-linejoin="round"><rect x="2.5" y="5" width="19" height="14" rx="1"/><path d="M2.5 6l9.5 7 9.5-7"/></svg>
          info@ridgelinehomes.com
        </li>
        <li>
          <svg viewBox="0 0 24 24" fill="none" stroke="#2fa944" stroke-width="2"><circle cx="12" cy="12" r="9.5"/><ellipse cx="12" cy="12" rx="4" ry="9.5"/><path d="M2.5 12h19M4 7h16M4 17h16"/></svg>
          www.ridgelinehomes.com
        </li>
      </ul>
    </div>
    <div class="contact__social"><span class="dot"></span>Ridgelinehomes/</div>
    <div class="contact__brand brand">
      <div class="brand__main">Ridgeline Homes</div>
      <div class="brand__sub">and Developments Pty Ltd</div>
    </div>
  </section>

</body>
</html>
```